Letterhead, envelope & business card design

We would like to refresh the look and feel of our business cards & letterheads.

Our company specialises in premium property.

We are looking for a unique minimalist design for our letterhead & business cards that project this.

I can send over examples of our current design to draw from, although Im looking for some one with creativity, yet focussed on a clean modern, minimalist design.
Updates

I have just uploaded our current letterhead.

We have just removed the 'swoosh' grey symbol, but would still like to keep some part of grey in the design if possible.

thanks in advance.

Just uploaded my details for business card.

Can we see examples with the light grey used as the secondary color?

thanks in advance.

Target Market(s)

We are a premium real estate agency & we want that message to be carried through our business cards & stationery.

Industry/Entity Type

Business

```html
<!DOCTYPE html>
<html lang="en">
<head>
<meta charset="utf-8">
<title>Harlow Estate Agents — Stationery</title>
<link href="https://fonts.googleapis.com/css2?family=Open+Sans:wght@400;600&display=swap" rel="stylesheet">
<style>
  :root{
    --bg:#dcdcdc;
    --paper:#ffffff;
    --navy:#0c3a52;
    --teal:#1f6d8a;
    --teal-light:#2a85a4;
    --grey:#9aa3a8;
    --ink:#0f4560;
  }
  html,body{margin:0;padding:0;overflow:hidden}
  body{width:688px;height:1200px;background:var(--bg);position:relative;font-family:"Open Sans",Arial,sans-serif}
  .sheet{position:absolute;background:var(--paper);box-shadow:0 2px 6px rgba(0,0,0,.18)}
  .company-name{font-family:"Open Sans",Arial,sans-serif;font-weight:600;color:var(--ink);line-height:1;white-space:nowrap}
  .band{position:absolute;left:0;width:100%}
  .band svg{display:block;width:100%;height:100%}
  .band-text{position:absolute;top:0;left:0;width:100%;height:100%;color:#fff;display:flex;align-items:center;white-space:nowrap}
  .band-text b{font-weight:600}
  .pin{display:inline-block;width:7px;height:7px;border:1px solid #fff;border-radius:50%;margin-right:5px;vertical-align:middle}

  /* Letterhead */
  .letterhead{left:111px;top:60px;width:473px;height:609px}
  .letterhead .company-name{position:absolute;top:48px;left:0;width:100%;text-align:center;font-size:20px}
  .letterhead .band{top:571px;height:20px}
  .letterhead .band-text{font-size:7.5px}

  /* Envelope */
  .envelope-flap{position:absolute;left:67px;top:696px;width:541px;height:66px}
  .envelope{left:67px;top:760px;width:541px;height:243px}
  .envelope .company-name{position:absolute;top:40px;left:26px;font-size:19px}
  .envelope .band{top:205px;height:24px}
  .envelope .band-text{font-size:10px}

  /* Business cards */
  .card{top:1023px;width:195px;height:110px}
  .card-front{left:121px;background:linear-gradient(180deg,#fff 0%,#f1f2f3 100%)}
  .card-front .person{position:absolute;top:7px;width:100%;text-align:center;color:var(--ink);font-size:7px;font-weight:600}
  .card-front .role{position:absolute;top:18px;width:100%;text-align:center;font-size:4px;color:var(--grey)}
  .card-front .company-name{position:absolute;top:48px;width:100%;text-align:center;font-size:10px}
  .card-front .valuer{position:absolute;top:70px;width:100%;text-align:center;font-size:4px;color:var(--grey)}
  .card-front .band{top:92px;height:10px}
  .card-front .band-text{font-size:4px}
  .card-back{left:339px;background:linear-gradient(90deg,var(--navy) 0%,var(--teal) 100%)}
  .card-back .company-name{position:absolute;top:50px;width:100%;text-align:center;font-size:10px;color:#fff}
</style>
</head>
<body>

<section class="sheet letterhead">
  <div class="company-name">Harlow Estate Agents</div>
  <div class="band">
    <svg viewBox="0 0 473 20" preserveAspectRatio="none">
      <rect x="0" y="4" width="473" height="16" fill="var(--navy)"/>
      <polygon points="0,0 236,0 226,16 0,16" fill="var(--teal)"/>
    </svg>
    <div class="band-text">
      <span style="margin-left:24px"><b>M:</b> 0400 555 218</span>
      <span style="margin-left:16px"><b>P:</b> 02 5550 1234</span>
      <span style="margin-left:auto">Registered Valuer 000 512</span>
      <span style="margin-left:12px;margin-right:22px"><i class="pin"></i>12 Harbour St, Westbay NSW 2000</span>
    </div>
  </div>
</section>

<svg class="envelope-flap" viewBox="0 0 541 66" preserveAspectRatio="none">
  <defs>
    <linearGradient id="flapGrad" x1="0" y1="0" x2="0" y2="1">
      <stop offset="0" stop-color="var(--teal-light)"/>
      <stop offset="1" stop-color="var(--navy)"/>
    </linearGradient>
  </defs>
  <path d="M0,66 L22,14 Q28,0 44,0 L497,0 Q513,0 519,14 L541,66 Z" fill="url(#flapGrad)"/>
</svg>

<section class="sheet envelope">
  <div class="company-name">Harlow Estate Agents</div>
  <div class="band">
    <svg viewBox="0 0 541 24" preserveAspectRatio="none">
      <rect x="0" y="5" width="541" height="19" fill="var(--navy)"/>
      <polygon points="0,0 246,0 232,19 0,19" fill="var(--teal)"/>
    </svg>
    <div class="band-text">
      <span style="margin-left:24px"><b>M:</b> 0400 555 218</span>
      <span style="margin-left:16px"><b>P:</b> 02 5550 1234</span>
      <span style="margin-left:auto;font-size:8px">Registered Valuer 000 512</span>
      <span style="margin-left:14px;margin-right:14px;font-size:8px"><i class="pin"></i>12 Harbour St, Westbay NSW 2000</span>
    </div>
  </div>
</section>

<section class="sheet card card-front">
  <div class="person">NED HARLOW</div>
  <div class="role">Director | Licensed Estate Agent</div>
  <div class="company-name">Harlow Estate Agents</div>
  <div class="valuer">Registered Valuer 000 512</div>
  <div class="band">
    <svg viewBox="0 0 195 10" preserveAspectRatio="none">
      <rect x="0" y="2" width="195" height="8" fill="var(--navy)"/>
      <polygon points="0,0 96,0 90,8 0,8" fill="var(--teal)"/>
    </svg>
    <div class="band-text">
      <span style="margin-left:8px"><b>M:</b> 0400 555 218</span>
      <span style="margin-left:6px"><b>P:</b> 02 5550 1234</span>
      <span style="margin-left:auto;margin-right:8px">12 Harbour St, Westbay NSW 2000</span>
    </div>
  </div>
</section>

<section class="sheet card card-back">
  <div class="company-name">Harlow Estate Agents</div>
</section>

</body>
</html>
```